New business card for my lawn and landscape business

Dorrin Yard and Building is a full-service lawn care, landscaping, and light construction company serving Paragould and the Northeast Arkansas region. The business is owned and operated by Marcus Toller, with a reputation for hands-on, detail-oriented service, dependable crews, and quality results for both residential and commercial clients. A well regarded business with great reviews.
Owner Marcus Toller
Dorrinyardandbuilding.example

Target Market(s)

Commercial, Middle, and upper class in north east Arkansas

Industry/Entity Type

Lawn maintenance and landscape

Contact Information for Business Card

Dorrin Yard And Building Professional lawn care, landscaping, and property improvement in Northeast Arkansas. • lawn maintenance •lawn treatments and weed control • exterior projects • Custom landscape design & installation • Sod, trees, rock & drainage solutions • Residential & commercial services Reliable. Detailed. Done right.

Requirements
Must have
• Business name, service area, list of some of our services, clean design that represents
Nice to have
• Unique. Different design element than just grass because its already in n the logo. Picture of a warm season (south) lawn or landscape. Pictures of the type of work we do

```html
<!DOCTYPE html>
<html lang="en">
<head>
<meta charset="utf-8">
<title>Dorrin Yard and Building – Business Card</title>
<link rel="stylesheet" href="https://fonts.googleapis.com/css2?family=Tinos:wght@400;700&display=swap">
<style>
  :root {
    --backdrop: #d4d5d4;
    --card: #f3f3f1;
    --green-dark: #1f6b34;
    --green-light: #6cbd3e;
  }
  html, body {
    margin: 0;
    padding: 0;
    width: 1200px;
    height: 1200px;
    overflow: hidden;
    background: var(--backdrop);
    font-family: "Tinos", "Times New Roman", serif;
  }
  .canvas {
    position: relative;
    width: 1200px;
    height: 1200px;
  }
  .card {
    position: absolute;
    top: 458px;
    width: 520px;
    height: 297px;
    background: var(--card);
    border-radius: 32px;
    overflow: hidden;
  }
  .card--front { left: 47px; }
  .card--back { left: 639px; }

  /* Front: services and name mark */
  .services {
    position: absolute;
    left: 19px;
    top: 92px;
    margin: 0;
    padding: 0;
    list-style: none;
    color: var(--green-dark);
    font-size: 14px;
    line-height: 17.6px;
  }
  .services li::before { content: "• "; }
  .divider {
    position: absolute;
    left: 318px;
    top: 49px;
    width: 3px;
    height: 194px;
    background: var(--green-light);
  }
  .brand {
    position: absolute;
    left: 352px;
    top: 126px;
    display: flex;
    align-items: center;
    gap: 8px;
  }
  .brand__dot {
    width: 14px;
    height: 14px;
    border-radius: 50%;
    background: var(--green-light);
    flex: none;
  }
  .brand__name {
    color: var(--green-dark);
    font-size: 16px;
    line-height: 19px;
    font-weight: 400;
  }
  .band {
    position: absolute;
    background: var(--green-light);
  }
  .band--front { left: 0; width: 242px; bottom: 0; height: 18px; }
  .band--back { left: 279px; width: 232px; top: 0; height: 14px; }

  /* Back: owner and contact */
  .owner {
    position: absolute;
    left: 32px;
    top: 24px;
    color: var(--green-dark);
  }
  .owner__name {
    margin: 0;
    font-size: 25px;
    line-height: 28px;
    font-weight: 400;
  }
  .owner__name strong { font-weight: 700; }
  .owner__role {
    margin: 0;
    font-size: 18px;
    line-height: 22px;
  }
  .website {
    position: absolute;
    right: 14px;
    top: 137px;
    display: flex;
    align-items: center;
    gap: 10px;
    color: var(--green-light);
    font-size: 15px;
  }
  .website svg { width: 17px; height: 17px; }
  .about {
    position: absolute;
    left: 32px;
    top: 214px;
    width: 300px;
    margin: 0;
    color: var(--green-light);
    font-size: 12px;
    line-height: 15px;
  }
</style>
</head>
<body>
<main class="canvas">
  <section class="card card--front" aria-label="Card front">
    <ul class="services">
      <li>lawn maintenance</li>
      <li>lawn treatments and weed control</li>
      <li>exterior projects</li>
      <li>Custom landscape design &amp; installation</li>
      <li>Sod, trees, rock &amp; drainage solutions</li>
      <li>Residential &amp; commercial services Reliable</li>
    </ul>
    <div class="divider"></div>
    <div class="brand">
      <span class="brand__dot"></span>
      <span class="brand__name">Dorrin Yard<br>and Building</span>
    </div>
    <div class="band band--front"></div>
  </section>

  <section class="card card--back" aria-label="Card back">
    <div class="band band--back"></div>
    <div class="owner">
      <h1 class="owner__name"><strong>Marcus</strong> Toller</h1>
      <p class="owner__role">Owner</p>
    </div>
    <div class="website">
      <span>Dorrinyardandbuilding.example</span>
      <svg viewBox="0 0 20 20" aria-hidden="true">
        <circle cx="10" cy="10" r="8.5" fill="none" stroke="#6cbd3e" stroke-width="1.8"/>
        <ellipse cx="10" cy="10" rx="3.6" ry="8.5" fill="none" stroke="#6cbd3e" stroke-width="1.5"/>
        <line x1="1.5" y1="10" x2="18.5" y2="10" stroke="#6cbd3e" stroke-width="1.5"/>
        <path d="M11 11 L18 14 L15 15 L17 19 L15.5 19.6 L13.6 15.8 L11.5 17.5 Z" fill="#6cbd3e" stroke="#f3f3f1" stroke-width="0.8"/>
      </svg>
    </div>
    <p class="about">Dorrin Yard And Building Professional lawn care, landscaping, and property improvement in Northeast Arkansas.</p>
  </section>
</main>
</body>
</html>
```